LoftHarbor - Coworking website design

LoftHarbor is a new global coworking brand, growing fast and establishing stylish locations and communities that inspire innovation and collaboration all around the world.
The project includes a complete website design, focused on delivering the company’s values and messages, provide information to site visitors and to generate leads.

Please review the attached design brief, for more information.

Target Market(s)

Both men and women. Decision makers in:
Small & medium businesses in various fields, but mainly technology firms (Startups or established brands).
Global enterprises.
Dynamic “new generation” companies.
Press

Number of Pages Required

2 page

Requirements
Must have
• Project Scope & deliverables:
• Concept and design for :
• Home page
• Deliver the values mentioned above.
• Showcase the cities in which the company has locations in.
• Show customer testimonials.
• Provide an interface (form) for booking a tour and/or leaving contact details for more information (two alternatives)
• Coworking location page - Each location is in the coolest part of a different major city, and has its own address, set of amenities (kitchen, fast internet etc,), area information (public transportation accessibility, sites near by, bars and restaurants in walking distance) and pricing for private offices (based on number of people per office). Each location page must have an interface to book a location tour.
• Site Navigation (header & footer) - allow simple navigation between multiple city pages, location pages and homepage. Growth of up to 50 locations in 25 cities.
• The navigation should account for Navigation to additional pages (not commissioned in this project) such as:
• Locations
• Enterprise
• Special promotions
• Blog
• Contact us
• About us
• Note - the site should account for geolocation variable display, showing different content for different locations.
• Deliverables must include all editable graphic files (photoshop or similar), as follows:
• Home page - Desktop view (preferably both)
• Location page - Mobile web view (preferably both)
• Navigation - both options

```html
<!DOCTYPE html>
<html lang="en">
<head>
<meta charset="utf-8">
<title>LoftHarbor — Coworking</title>
<link href="https://fonts.googleapis.com/css2?family=Open+Sans:wght@400;600;700&family=Roboto+Condensed:wght@400;700&display=swap" rel="stylesheet">
<style>
:root{
  --orange:#f2a20c;
  --orange-dark:#e39500;
  --ink:#222222;
  --text:#666666;
  --muted:#8a8a8a;
  --light:#f3f3f3;
  --line:#dddddd;
  --white:#ffffff;
}
*{box-sizing:border-box;margin:0;padding:0}
html,body{width:1200px;height:4737px;overflow:hidden;background:var(--white)}
body{position:relative;font-family:"Open Sans",Arial,sans-serif;color:var(--text);font-size:15px;line-height:1.55}
.abs{position:absolute}
.head{font-family:"Roboto Condensed","Arial Narrow",sans-serif;color:var(--ink);font-weight:700;text-transform:uppercase}
.btn{position:absolute;background:var(--orange);color:var(--white);font-family:"Roboto Condensed",sans-serif;font-weight:700;font-size:13px;text-transform:uppercase;display:flex;align-items:center;justify-content:center;letter-spacing:.5px}
.photo{position:absolute}

/* header */
.brand{left:120px;top:40px;font-family:"Roboto Condensed",sans-serif;font-weight:700;font-size:38px;color:var(--orange);line-height:1}
.login{left:995px;top:28px;width:82px;height:24px;font-size:13px}
.nav{left:510px;top:62px;display:flex;gap:26px;font-family:"Roboto Condensed",sans-serif;font-weight:700;font-size:15px;color:var(--ink);text-transform:uppercase}
.nav .active{position:relative}
.nav .active::after{content:"";position:absolute;left:0;right:0;top:36px;height:4px;background:var(--orange)}

/* hero */
.hero{left:0;top:110px;width:1200px;height:616px;background:linear-gradient(100deg,#5b5046 0%,#8c8278 35%,#6e6a62 60%,#3f3b36 100%)}
.hero-title{left:0;width:1200px;top:398px;text-align:center;color:var(--white);font-size:36px}
.hero-sub{left:420px;width:360px;top:444px;text-align:center;color:var(--white);font-size:15px;line-height:1.4}
.hero-btn{left:541px;top:490px;width:128px;height:32px}
.dots{display:flex;gap:9px}
.dots span{width:9px;height:9px;border-radius:50%;background:#c9c9c9}
.dots span.on{background:var(--orange)}
.hero-dots{left:582px;top:628px}

/* search */
.search{left:0;top:726px;width:1200px;height:206px;background:var(--light)}
.search-label{font-size:13px;color:var(--ink);font-weight:600}
.field{position:absolute;background:var(--white);border:1px solid var(--line);height:36px;font-size:12px;color:var(--ink);display:flex;align-items:center;padding-left:12px}
.seg{position:absolute;top:818px;height:36px;background:var(--white);border:1px solid var(--line);width:85px;font-size:12px;color:var(--ink);display:flex;align-items:center;justify-content:center}

/* about */
.about-title{left:120px;top:1052px;font-size:30px;text-transform:none}
.about-text{left:120px;top:1098px;width:485px;font-size:13px;line-height:1.55}
.about-btn{left:120px;top:1318px;width:128px;height:34px}

/* enterprise */
.sec-title{left:0;width:1200px;text-align:center;font-size:30px}
.sec-sub{left:400px;width:400px;text-align:center;font-size:14px;line-height:1.45}
.card-cap{width:300px;text-align:center;font-size:17px}

/* promotions */
.kicker{font-family:"Roboto Condensed",sans-serif;color:var(--muted);font-size:15px;text-transform:uppercase}
.body-copy{font-size:13px;line-height:1.5}
.tabs{left:120px;top:2476px;display:flex;gap:38px;font-family:"Roboto Condensed",sans-serif;font-weight:700;font-size:15px;color:var(--ink);text-transform:uppercase}
.tabs .active{border-bottom:3px solid var(--orange);padding-bottom:6px}

/* benefits */
.benefits{left:0;top:2785px;width:1200px;height:610px;background:var(--light)}
.benefit{width:260px;text-align:center}
.benefit svg{display:block;margin:0 auto 14px}
.benefit h4{font-family:"Roboto Condensed",sans-serif;font-weight:700;font-size:16px;color:var(--ink);text-transform:uppercase;margin-bottom:10px}
.benefit p{font-size:13px;line-height:1.5}

/* blog / testimonials */
.meta{font-size:12px;color:var(--muted)}
.quote{font-family:Georgia,serif;font-size:34px;color:var(--ink);line-height:1}

/* contact */
.map{left:0;top:3932px;width:600px;height:451px;background:linear-gradient(135deg,#e9e9e9,#d7d7d7)}
.contact{left:600px;top:3932px;width:600px;height:451px;background:var(--orange)}
.contact-title{left:645px;top:3962px;font-size:16px;color:var(--white)}
.contact-field{position:absolute;left:645px;width:448px;background:var(--white);font-size:13px;color:var(--ink);padding:8px 12px}
.send{left:645px;top:4268px;width:128px;height:32px;background:var(--white);color:var(--ink)}
.map-title{left:100px;top:3962px;font-size:16px;color:var(--orange)}

/* footer */
.foot-brand{left:120px;top:4448px;font-family:"Roboto Condensed",sans-serif;font-weight:700;font-size:34px;color:var(--orange);line-height:1}
.foot-head{font-family:"Roboto Condensed",sans-serif;font-weight:700;font-size:13px;color:var(--orange);text-transform:uppercase}
.foot-list{font-size:13px;color:var(--ink);line-height:1.45}
.bottom{left:0;top:4690px;width:1200px;height:47px;background:var(--orange)}
.bottom-links{left:120px;top:4705px;color:var(--white);font-family:"Roboto Condensed",sans-serif;font-weight:700;font-size:13px;text-transform:uppercase;letter-spacing:.4px}
.social{left:960px;top:4700px;display:flex;gap:14px}
.social span{width:28px;height:28px;border-radius:50%;background:var(--white)}
</style>
</head>
<body>

<!-- Header -->
<header>
  <div class="abs brand">LoftHarbor</div>
  <div class="btn login">Login</div>
  <nav class="abs nav">
    <span class="active">Locations</span><span>Enterprise</span><span>Special Promotions</span><span>Blog</span><span>Contact</span><span>About</span>
  </nav>
</header>

<!-- Hero -->
<section>
  <div class="photo hero" role="img" aria-label="Bright open-plan coworking office with people working at desks"></div>
  <h1 class="abs head hero-title">Brand Personality</h1>
  <p class="abs hero-sub">Brand personality is a set of human characteristics that are attributed to a brand name.</p>
  <div class="btn hero-btn">Read More</div>
  <div class="abs dots hero-dots"><span></span><span class="on"></span><span></span></div>
</section>

<!-- Search -->
<section>
  <div class="abs search"></div>
  <div class="abs search-label" style="left:180px;top:792px">Where you'd like space</div>
  <div class="field" style="left:180px;top:818px;width:342px">Choose &amp; Location</div>
  <div class="abs search-label" style="left:560px;top:792px">How many employee</div>
  <div class="seg" style="left:560px">1-20</div>
  <div class="seg" style="left:644px">20-100</div>
  <div class="seg" style="left:728px">100-1,000</div>
  <div class="seg" style="left:812px">1,000+</div>
  <div class="btn" style="left:925px;top:818px;width:125px;height:36px">Start</div>
</section>

<!-- About -->
<section>
  <div class="photo" style="left:1001px;top:932px;width:199px;height:142px;background:linear-gradient(135deg,#d9d5cf,#8a7b6c)" role="img" aria-label="Coffee cup on a desk beside a notebook"></div>
  <h2 class="abs head about-title">LoftHarbor</h2>
  <p class="abs about-text">Brand personality is a set of human characteristics that are attributed to a brand name. A brand personality is something to which the consumer can relate; an effective brand increases its brand equity by having a consistent set of traits that a specific consumer segment enjoys. This personality is a qualitative value-add that a brand gains, in addition to its functional benefits. The brand personality gives consumers something with which they can relate effectively increasing brand awareness and popularity.<br><br>When we are what we say, personality is how we say it - our tone of voice.</p>
  <div class="btn about-btn">Read More</div>
  <div class="photo" style="left:632px;top:1033px;width:442px;height:293px;background:linear-gradient(160deg,#e8e6e2,#a9a49c 60%,#6d6a66)" role="img" aria-label="Lounge area of a coworking space with sofas and blue pendant lights"></div>
</section>

<!-- Enterprise -->
<section>
  <h2 class="abs head sec-title" style="top:1438px">Enterprise</h2>
  <p class="abs sec-sub" style="top:1480px">Lorem Ipsum is simply dummy text of the printing and typesetting industry.</p>
  <div class="photo" style="left:120px;top:1550px;width:300px;height:272px;background:linear-gradient(135deg,#3a3430,#7a6e62)" role="img" aria-label="Hands typing on a laptop"></div>
  <div class="photo" style="left:451px;top:1550px;width:298px;height:272px;background:linear-gradient(135deg,#d8d8d6,#7c7c7a)" role="img" aria-label="Meeting room with a long table and chairs"></div>
  <div class="photo" style="left:780px;top:1550px;width:300px;height:272px;background:linear-gradient(135deg,#cfd3d6,#6f7478)" role="img" aria-label="People working on laptops in a bright office"></div>
  <div class="abs head card-cap" style="left:120px;top:1843px">Global Access</div>
  <div class="abs head card-cap" style="left:450px;top:1843px">Global Teams</div>
  <div class="abs head card-cap" style="left:780px;top:1843px">Signature Design</div>
  <div class="btn" style="left:541px;top:1902px;width:118px;height:32px">View More</div>
</section>

<!-- Special promotions -->
<section>
  <div class="photo" style="left:120px;top:2062px;width:480px;height:316px;background:linear-gradient(135deg,#e7e7e7,#9ea7b0 55%,#4d5660)" role="img" aria-label="Man working at a desktop computer"></div>
  <div class="abs kicker" style="left:632px;top:2070px">Why DeskNest</div>
  <h2 class="abs head" style="left:632px;top:2094px;font-size:30px">Special Promotions</h2>
  <p class="abs body-copy" style="left:632px;top:2142px;width:448px">Lorem Ipsum is simply dummy text of the printing and typesetting industry. Lorem Ipsum has been the industry's standard dummy text ever since the 1500s, when an unknown printer took a galley of type and scrambled it to make a type specimen book. It has survived not only five centuries</p>
  <div class="btn" style="left:632px;top:2266px;width:128px;height:32px">Read More</div>

  <h2 class="abs head" style="left:120px;top:2418px;font-size:30px">Our Services</h2>
  <div class="abs tabs"><span class="active">Workspace</span><span>Events</span><span>Network</span><span>Innovation</span></div>
  <p class="abs body-copy" style="left:120px;top:2530px;width:460px">Lorem Ipsum is simply dummy text of the printing and typesetting industry. Lorem Ipsum has been the industry's standard dummy text ever since the 1500s,<br>when an unknown printer took a galley of typeset scrambled it to make a type specimen book. It has survived not only five centuries</p>
  <div class="btn" style="left:120px;top:2662px;width:128px;height:32px">Read More</div>
  <div class="photo" style="left:600px;top:2381px;width:480px;height:322px;background:linear-gradient(135deg,#2b2b2b,#8a8a8a 60%,#c8362b)" role="img" aria-label="Hand writing notes beside a laptop"></div>
</section>

<!-- Benefits -->
<section>
  <div class="abs benefits"></div>
  <h2 class="abs head sec-title" style="top:2858px">Our Benefits</h2>

  <div class="abs benefit" style="left:88px;top:2940px">
    <svg width="54" height="44" viewBox="0 0 54 44" fill="none" stroke="#f2a20c" stroke-width="4" stroke-linecap="round"><path d="M5 16a31 31 0 0 1 44 0"/><path d="M13 24a20 20 0 0 1 28 0"/><path d="M21 32a9 9 0 0 1 12 0"/><circle cx="27" cy="39" r="2.5" fill="#f2a20c"/></svg>
    <h4>Fast Internet</h4><p>Lorem Ipsum is simply dummy text<br>of the printing and typesetting<br>industry ⊕</p>
  </div>
  <div class="abs benefit" style="left:467px;top:2940px">
    <svg width="44" height="48" viewBox="0 0 44 48" fill="none" stroke="#f2a20c" stroke-width="3.5" stroke-linejoin="round"><rect x="4" y="3" width="36" height="36" rx="5"/><path d="M4 24h36M4 12h36"/><circle cx="12" cy="31" r="2.5"/><circle cx="32" cy="31" r="2.5"/><path d="M10 39v6M34 39v6"/></svg>
    <h4>Public Transportation</h4><p>Lorem Ipsum is simply dummy text<br>of the printing and typesetting<br>industry ⊕</p>
  </div>
  <div class="abs benefit" style="left:824px;top:2940px">
    <svg width="50" height="48" viewBox="0 0 50 48" fill="none" stroke="#f2a20c" stroke-width="3.5" stroke-linecap="round"><path d="M15 4c-3 4 3 6 0 10M24 4c-3 4 3 6 0 10M33 4c-3 4 3 6 0 10"/><path d="M6 20h34v10a14 14 0 0 1-14 14h-6A14 14 0 0 1 6 30z"/><path d="M40 24h3a4 4 0 0 1 0 8h-4"/></svg>
    <h4>Kitchen</h4><p>Lorem Ipsum is simply dummy text<br>of the printing and typesetting<br>industry ⊕</p>
  </div>

  <div class="abs benefit" style="left:88px;top:3140px">
    <svg width="48" height="44" viewBox="0 0 48 44" fill="none" stroke="#f2a20c" stroke-width="3.5" stroke-linecap="round"><path d="M4 32h40M8 32a16 16 0 0 1 32 0"/><path d="M24 12V8M20 8h8"/><path d="M2 38h44"/></svg>
    <h4>Restaurants</h4><p>Lorem Ipsum is simply dummy text<br>of the printing and typesetting<br>industry ⊕</p>
  </div>
  <div class="abs benefit" style="left:467px;top:3140px">
    <svg width="70" height="44" viewBox="0 0 70 44" fill="none" stroke="#f2a20c" stroke-width="3.5"><circle cx="14" cy="14" r="6"/><circle cx="35" cy="12" r="7"/><circle cx="56" cy="14" r="6"/><path d="M3 38a11 11 0 0 1 22 0M22 38a13 13 0 0 1 26 0M45 38a11 11 0 0 1 22 0"/></svg>
    <h4>Number of People Per</h4><p>Lorem Ipsum is simply dummy text<br>of the printing and typesetting<br>industry ⊕</p>
  </div>
  <div class="abs benefit" style="left:824px;top:3140px">
    <svg width="44" height="48" viewBox="0 0 44 48" fill="none" stroke="#f2a20c" stroke-width="3.5" stroke-linejoin="round"><rect x="4" y="4" width="22" height="40"/><rect x="26" y="20" width="14" height="24"/><path d="M10 12h4M16 12h4M10 20h4M16 20h4M10 28h4M16 28h4M13 44v-8"/></svg>
    <h4>Offices</h4><p>Lorem Ipsum is simply dummy text<br>of the printing and typesetting<br>industry ⊕</p>
  </div>
</section>

<!-- Blog & Testimonials -->
<section>
  <h2 class="abs head" style="left:120px;top:3470px;font-size:28px">Our Blog</h2>
  <p class="abs" style="left:120px;top:3508px;font-size:14px">Lorem Ipsum is simply dummy text of the industry.</p>
  <div class="photo" style="left:126px;top:3569px;width:202px;height:214px;background:linear-gradient(135deg,#c9c4bd,#7f756a)" role="img" aria-label="Group of colleagues talking around a table"></div>
  <div class="abs head" style="left:341px;top:3574px;font-size:15px">Cloud Coworking</div>
  <div class="abs meta" style="left:341px;top:3598px">◷ November 02, 2017 &nbsp;&nbsp; ♡ 33</div>
  <p class="abs" style="left:341px;top:3625px;width:225px;font-size:13px;line-height:1.5">Lorem Ipsum is simply dummy text of the printing and typesetting industry. Lorem Ipsum has been the industry's standard dummy text ever since the 1500s.</p>
  <div class="abs" style="left:341px;top:3732px;font-size:13px;color:var(--ink)">Read More ⊕</div>
  <div class="abs dots" style="left:341px;top:3766px"><span class="on"></span><span></span><span></span></div>
  <div class="btn" style="left:366px;top:3832px;width:120px;height:32px">View More</div>

  <h2 class="abs head" style="left:600px;top:3470px;font-size:28px">Testimonials</h2>
  <p class="abs" style="left:600px;top:3508px;font-size:14px">Lorem Ipsum is simply dummy text of the industry.</p>
  <div class="photo" style="left:603px;top:3569px;width:209px;height:214px;background:linear-gradient(135deg,#e2e0dc,#a8a098)" role="img" aria-label="Portrait of a smiling client in an office"></div>
  <div class="abs head" style="left:834px;top:3574px;font-size:15px">Feedback</div>
  <div class="abs head" style="left:834px;top:3598px;font-size:16px">Daniel Moore</div>
  <div class="abs" style="left:834px;top:3620px;font-size:12px;color:var(--ink);font-weight:600">Creative Director</div>
  <div class="abs quote" style="left:834px;top:3644px">“</div>
  <p class="abs" style="left:834px;top:3672px;width:222px;font-size:13px;line-height:1.45;color:var(--ink)">Lorem Ipsum is simply dummy text of the printing and typesetting industry. Lorem Ipsum has been the industry's standard dummy</p>
  <div class="abs quote" style="left:1062px;top:3728px">”</div>
  <div class="abs dots" style="left:834px;top:3766px"><span class="on"></span><span></span><span></span></div>
  <div class="btn" style="left:830px;top:3832px;width:120px;height:32px">View More</div>
</section>

<!-- Map & Contact -->
<section>
  <div class="photo map" role="img" aria-label="World map showing company locations"></div>
  <div class="abs head map-title">Location Map</div>
  <div style="position:absolute;left:100px;top:3988px;width:120px;height:3px;background:var(--orange)"></div>
  <svg class="abs" style="left:294px;top:4100px" width="34" height="46" viewBox="0 0 34 46"><path d="M17 2C8.7 2 2 8.7 2 17c0 11 15 27 15 27s15-16 15-27C32 8.7 25.3 2 17 2z" fill="#f2a20c"/><circle cx="17" cy="17" r="6" fill="#fff"/></svg>

  <div class="abs contact"></div>
  <div class="abs head contact-title">Quick Contact</div>
  <div style="position:absolute;left:645px;top:3988px;width:120px;height:3px;background:var(--white)"></div>
  <div class="contact-field" style="top:4024px;height:34px">Name</div>
  <div class="contact-field" style="top:4090px;height:34px">Phone</div>
  <div class="contact-field" style="top:4152px;height:86px">Message</div>
  <div class="btn send">Send</div>
</section>

<!-- Footer -->
<footer>
  <div class="abs foot-brand">LoftHarbor</div>
  <p class="abs" style="left:120px;top:4500px;width:230px;font-size:13px;line-height:1.5;color:var(--ink)">Lorem Ipsum is simply dummy text of the printing and types etting industry. Lorem Ipsum is the industry's ...</p>
  <div class="abs" style="left:120px;top:4600px;font-size:13px;color:var(--ink)">Read More.. ⊕</div>

  <div class="abs foot-head" style="left:385px;top:4450px">Quick Links</div>
  <div class="abs foot-list" style="left:385px;top:4498px">Locations<br>Enterprise<br>Special<br>Promotions<br>Blog<br>Contact us<br>About us</div>

  <div class="abs foot-head" style="left:556px;top:4450px">Address</div>
  <div class="abs foot-list" style="left:556px;top:4498px">18 Pier Lane,<br>Suite 40, USA<br><br>+00 100 200 3000<br><br>info@loftharbor.com<br><br>Mon-Sat 9:00am-6:00pm</div>

  <div class="abs foot-head" style="left:800px;top:4450px">Subscribe</div>
  <div class="abs" style="left:800px;top:4498px;font-size:13px;color:var(--ink)">Get the latest updates and offer.</div>
  <div class="field" style="left:800px;top:4532px;width:240px;height:38px">Enter Your Email</div>
  <div class="btn" style="left:1040px;top:4532px;width:44px;height:38px">
    <svg width="20" height="14" viewBox="0 0 20 14" fill="none" stroke="#fff" stroke-width="2"><rect x="1" y="1" width="18" height="12"/><path d="M1 1l9 7 9-7"/></svg>
  </div>

  <div class="abs bottom"></div>
  <div class="abs bottom-links">Privacy Policy · Legal Mentions · Terms and Conditions</div>
  <div class="abs social"><span></span><span></span><span></span><span></span><span></span></div>
</footer>

</body>
</html>
```